макет для напольного лайтбокса Walltop Media
Задание на дизайн
Где будет использоваться баннер?
в Бизнес - Центрах
Какое название (бизнеса, или всей компании) должно использоваться дизайнерами?
Walltop Media реклама в Бизнес-Центрах
Необходимо сделать новый дизайн нашего макета для рекламных носителей в 2-ух вариантах : вертикальный 1200*1800, горизонтальный 1800*1200
Основной цвет - консервативный темно-синий.
шрифт текста - Ариал.
Важно - новый логотип сделан с переливом, базовый темно-синий CMYK 100 75 15 0.
- эффект полупрозрачных снисходящих окон.
Информацию размещаем по минимуму - 3 блока сверху вниз:
www.walltop-media.ru
ЛОГО
Walltop Media
Рекама в бизнес-центрах
WALLTOP MEDIA - федеральный оператор рекламы в бизнес-центрах. По вопросу размещения рекламы обращайтесь по тел: +7 (495) 318-52-07 или оставьте заявку на сайте www.walltop-media.ru.Специальные условия размещения для компаний арендаторов.
В аттаче смотрите приблизительные варианты.
В центре оставляем лого+название.
хочется, чтобы постер был минималистичен и при этом передавал ощущение консервативности и солидности.
Высылаю исходники лого. Но обратите внимание - в исходниках, тот логотип, который выполнен переливом двух цветов, темно-синий неправильный. Правильный - CMYK 100 75 15 0. Светлый можно оставить.
Какой товар или услуга будет рекламироваться?
туризм, еда, такси
Реклама
Размер баннера
наш логотип
Комментарии и пожелания для дизайнеров
Нужна ли картинка на задний план - не знаю, но если будет только текст, будет плохо.
Важный ориентир - макет постера должен создавать ощущение солидности, т.к. постер должен органично вписываться в интерьер премиального БЦ класса А.

```html
<!DOCTYPE html>
<html lang="ru">
<head>
<meta charset="utf-8">
<title>Walltop Media — постер для лайтбокса</title>
<link rel="stylesheet" href="https://fonts.googleapis.com/css2?family=Arimo:wght@400;700&display=swap">
<style>
  :root {
    --stage: #05478a;
    --paper: #ffffff;
    --brand-blue: #05468a;
    --brand-blue-light: #2f6aa8;
    --shadow-grey: #b3b1b2;
    --ink-light: #ffffff;
  }
  html, body {
    margin: 0;
    padding: 0;
    width: 954px;
    height: 1200px;
    overflow: hidden;
    background: var(--stage);
  }
  .canvas {
    position: relative;
    width: 954px;
    height: 1200px;
  }
  .poster {
    position: absolute;
    left: 117px;
    top: 59px;
    width: 720px;
    height: 1082px;
    display: block;
  }
  .poster text {
    font-family: "Arimo", Arial, sans-serif;
    font-weight: 700;
  }
  .contact-phone { font-size: 34px; fill: var(--ink-light); }
  .contact-site { font-size: 26px; fill: var(--ink-light); }
  .brand-name { font-size: 60px; fill: var(--brand-blue); }
  .brand-tagline { font-size: 32px; fill: var(--brand-blue); font-weight: 400 !important; letter-spacing: 0.5px; }
  .about-text { font-size: 17px; fill: var(--ink-light); }
  .paper { fill: var(--paper); }
  .fold-shade { fill: var(--shadow-grey); }
  .panel { fill: var(--brand-blue); }
  .brand-square { fill: var(--brand-blue); }
</style>
</head>
<body>
<main class="canvas">
  <svg class="poster" viewBox="0 0 770 1157" xmlns="http://www.w3.org/2000/svg" aria-label="Постер Walltop Media">
    <defs>
      <linearGradient id="ribbon-sheen" x1="0" y1="0" x2="1" y2="0.6">
        <stop offset="0" stop-color="#ffffff" stop-opacity="0"/>
        <stop offset="1" stop-color="#ffffff" stop-opacity="0.12"/>
      </linearGradient>
      <linearGradient id="brand-square-fill" x1="0" y1="0" x2="0" y2="1">
        <stop offset="0" stop-color="var(--brand-blue-light)"/>
        <stop offset="1" stop-color="var(--brand-blue)"/>
      </linearGradient>
    </defs>

    <rect class="paper" x="0" y="0" width="770" height="1157"/>

    <!-- top ribbon -->
    <g class="ribbon">
      <polygon class="fold-shade" points="86,0 125,0 125,302"/>
      <polygon class="fold-shade" points="644,0 683,0 644,302"/>
      <polygon class="fold-shade" points="125,302 384,201 644,302 384,216"/>
      <polygon class="panel" points="125,0 644,0 644,302 384,201 125,302"/>
      <polygon fill="url(#ribbon-sheen)" points="125,0 644,0 644,302 384,201 125,302"/>
      <text class="contact-phone" x="384" y="115" text-anchor="middle">+7 (495) 318 52 07</text>
      <text class="contact-site" x="384" y="149" text-anchor="middle">www.walltop-media.ru</text>
    </g>

    <!-- brand block -->
    <g class="brand">
      <rect class="brand-square" x="329" y="455" width="110" height="110" fill="url(#brand-square-fill)"/>
      <text class="brand-name" x="384" y="659" text-anchor="middle" textLength="519" lengthAdjust="spacingAndGlyphs">Walltop Media</text>
      <text class="brand-tagline" x="384" y="705" text-anchor="middle" textLength="519" lengthAdjust="spacingAndGlyphs">Реклама в бизнес-центрах</text>
    </g>

    <!-- bottom info panel -->
    <g class="info-panel">
      <rect class="fold-shade" x="125" y="763" width="519" height="10"/>
      <rect class="panel" x="125" y="773" width="519" height="384"/>
      <polygon fill="#ffffff" fill-opacity="0.08" points="125,773 260,773 125,980"/>
      <text class="about-text" text-anchor="middle">
        <tspan x="384" y="986">WALLTOP MEDIA - федеральный оператор рекламы</tspan>
        <tspan x="384" y="1007">в бизнес-центрах. По вопросу размещения рекламы</tspan>
        <tspan x="384" y="1028">обращайтесь по тел: +7 (495) 318-52-07 или</tspan>
        <tspan x="384" y="1050">оставьте заявку на сайте www.walltop-media.ru.</tspan>
        <tspan x="384" y="1071">Специальные условия размещения для</tspan>
        <tspan x="384" y="1092">компаний арендаторов.</tspan>
      </text>
    </g>
  </svg>
</main>
</body>
</html>
```